Electrical & Communications Company Wordpress Themed Website Design

Hi everyone,

I need a wordpress themed website designed for a new company based in Sydney Australia called "VELTRIX". It delivers electrical and communication services to the domestic and commercial sectors.

It needs to be the FULL/COMPLETE wordpress theme! A clean and easy to use site.

Please guys take the time to look at these competitors sites:

www.tapnovo.com.au
www.harbelwiring.com.au
www.qul.com.au
www.lumavoltics.com.au
www.corbinwiring.com.au
www.fendrasparkies.com.au

Please use these site for ideas only!!! we want to be original.

(If you would like to add electrical and communications to the logo that is O.K.)

Note: These logo's are registered trademarks of veltrix pty ltd.

Accreditation:

Ubta member (Federated wiring and signalling guild)

PLEASE CHECK THE WEB PLANNING LAYOUT BELOW FOR ROUGH IDEA
Updates

Have requested to increase payment to $400 and now guarantee payment!

Hi guys, forgot to mention i would like to see the business phone number prominently some where with a call to action.As we are a service business and need people to easly be able to see our contact number. Maybe top right courner but open to ideas. 

 Guys/Girls this is for a complete working word press theme that i can load up on the sever and access thru wordpress admin. Code etc

Industry/Entity Type

Communications

Requirements
Must have
• - Logo Provided must be used
• - Themes and colours to be consisted with with brand
• - Fully customizable
• - Have a social share button from shariq.com
• - Must be the full/complete theme for word press
Nice to have
• - pixtorvault
• - contactform
• - would like zenda orbit pay quidlo displayed
• - Guarantee logo or something
Should not have
• - Please don't waste your or our time submitting templates or copies of other sites original only!

```html
<!DOCTYPE html>
<html lang="en">
<head>
<meta charset="utf-8">
<title>Veltrix – Services</title>
<link href="https://fonts.googleapis.com/css2?family=Arimo:wght@400;700&family=PT+Sans:wght@400;700&display=swap" rel="stylesheet">
<style>
  :root {
    --brand-red: #e20f1e;
    --page-white: #ffffff;
    --bar-grey: #7d7d7d;
    --panel-grey: #5a5a5a;
    --footer-grey: #5c5c5c;
    --text-dark: #111111;
    --divider: #8c8c8c;
    --active-black: #1c1c1c;
  }
  * { box-sizing: border-box; margin: 0; padding: 0; }
  html, body { width: 1200px; height: 900px; overflow: hidden; }
  body {
    background: var(--brand-red);
    font-family: "PT Sans", sans-serif;
    position: relative;
  }
  .page {
    position: absolute; left: 219px; top: 0;
    width: 760px; height: 900px;
    background: var(--page-white);
  }
  .site-header { position: absolute; inset: 0 0 auto 0; height: 133px; }
  .brand { position: absolute; left: 26px; top: 18px; display: flex; align-items: center; gap: 14px; }
  .brand-mark { width: 92px; height: 92px; border-radius: 50%; border: 5px solid var(--brand-red); }
  .brand-name { font-family: "Arimo", sans-serif; font-weight: 700; font-size: 21px; color: var(--text-dark); line-height: 1; }
  .brand-tagline { font-family: "Arimo", sans-serif; font-size: 11px; color: #555; margin-top: 2px; }
  .header-divider { position: absolute; top: 12px; width: 2px; height: 105px; background: var(--divider); }
  .header-divider.first { left: 296px; }
  .header-divider.second { left: 531px; }
  .agent-photo {
    position: absolute; left: 343px; top: 30px; width: 55px; height: 84px;
    background: linear-gradient(180deg, #d9b48c, #bfc3c8 60%, #e9ecef);
    border-radius: 26px 26px 4px 4px;
  }
  .call-cta { position: absolute; left: 406px; top: 50px; }
  .call-label { font-family: "Arimo", sans-serif; font-size: 17px; color: var(--text-dark); line-height: 1.1; }
  .call-number { font-family: "Arimo", sans-serif; font-weight: 700; font-size: 15px; color: var(--brand-red); }
  .account { position: absolute; left: 557px; top: 18px; font-family: "Arimo", sans-serif; font-size: 10px; color: var(--text-dark); }
  .account-links { position: absolute; left: 64px; top: 0; white-space: nowrap; }
  .account-field { position: absolute; display: flex; align-items: center; white-space: nowrap; font-weight: 700; }
  .account-field label { width: 54px; text-align: right; margin-right: 10px; }
  .account-field span { width: 93px; height: 13px; border: 1px solid #999; display: block; }
  .field-user { left: 0; top: 23px; }
  .field-pass { left: 0; top: 40px; }
  .hero {
    position: absolute; left: 0; top: 133px; width: 760px; height: 195px;
    background: linear-gradient(180deg, #07090f 0%, #111a2b 55%, #2a2418 80%, #0b1320 100%);
  }
  .main-nav {
    position: absolute; left: 0; top: 328px; width: 760px; height: 25px;
    background: var(--bar-grey); display: flex; align-items: center;
    font-size: 14px; color: #fff;
  }
  .main-nav a { color: inherit; text-decoration: none; position: absolute; top: 4px; }
  .main-nav a.current { color: var(--brand-red); }
  .nav-sep { position: absolute; top: 9px; width: 1px; height: 9px; background: #fff; }
  .section-title { position: absolute; left: 47px; top: 401px; font-size: 14px; color: var(--brand-red); }
  .service-panel {
    position: absolute; left: 33px; top: 428px; width: 477px; height: 320px;
    background: var(--panel-grey); color: #fff;
  }
  .service-list { position: absolute; left: 0; top: 12px; width: 162px; list-style: none; font-size: 12px; }
  .service-list li { padding: 0 0 0 77px; height: 18px; line-height: 15px; }
  .service-list li.active { background: var(--active-black); height: 15px; margin-bottom: 3px; }
  .panel-divider { position: absolute; left: 175px; top: 13px; width: 2px; height: 292px; background: #fff; }
  .service-copy { position: absolute; left: 202px; top: 10px; width: 240px; font-size: 11.3px; line-height: 16.4px; }
  .sidebar-card { position: absolute; left: 545px; width: 179px; }
  .card-offers { top: 429px; }
  .card-reviews { top: 600px; }
  .card-title { height: 25px; background: var(--bar-grey); color: #fff; font-size: 13px; line-height: 26px; text-align: center; }
  .card-photo { height: 120px; }
  .card-offers .card-photo { background: linear-gradient(135deg, #cfd8e3, #4c79b8 60%, #2f5ea3); }
  .card-reviews .card-photo { background: linear-gradient(135deg, #c8a07c, #8d6a52 50%, #d4d1c8); }
  .site-footer {
    position: absolute; left: 0; top: 867px; width: 760px; height: 33px;
    background: var(--footer-grey); color: #fff;
  }
  .copyright { position: absolute; left: 198px; top: 12px; font-size: 10px; }
  .footer-sep { position: absolute; left: 339px; top: 8px; width: 2px; height: 17px; background: #111; }
  .footer-links { position: absolute; left: 357px; top: 10px; font-size: 12px; }
</style>
</head>
<body>
  <div class="page">
    <header class="site-header">
      <div class="brand">
        <div class="brand-mark"></div>
        <div>
          <div class="brand-name">VELTRIX</div>
          <div class="brand-tagline">communication solutions</div>
        </div>
      </div>
      <div class="header-divider first"></div>
      <div class="agent-photo" role="img" aria-label="Customer service agent wearing a headset"></div>
      <div class="call-cta">
        <div class="call-label">Call Us Now :</div>
        <div class="call-number">1300 418 27</div>
      </div>
      <div class="header-divider second"></div>
      <div class="account">
        <div class="account-links">Register | Login :</div>
        <div class="account-field field-user"><label>User:</label><span></span></div>
        <div class="account-field field-pass"><label>Password:</label><span></span></div>
      </div>
    </header>

    <div class="hero" role="img" aria-label="Sydney harbour bridge and city skyline at night"></div>

    <nav class="main-nav">
      <a style="left:44px">home</a><span class="nav-sep" style="left:103px"></span>
      <a style="left:134px">About</a><span class="nav-sep" style="left:200px"></span>
      <a class="current" style="left:221px">Services</a><span class="nav-sep" style="left:298px"></span>
      <a style="left:321px">guarantee</a><span class="nav-sep" style="left:405px"></span>
      <a style="left:435px">Policy</a><span class="nav-sep" style="left:512px"></span>
      <a style="left:540px">careers</a><span class="nav-sep" style="left:625px"></span>
      <a style="left:671px">contact</a>
    </nav>

    <h1 class="section-title" style="font-weight:400">Services :</h1>

    <section class="service-panel">
      <ul class="service-list">
        <li class="active">Communication</li>
        <li>Electrical</li>
      </ul>
      <div class="panel-divider"></div>
      <p class="service-copy">For great same day service when you need an electrician in Sydney, you can rely on the rapid on-time response, up-front per job pricing and professional red carpet service you receive from Fendra Electrical Services.&nbsp; Already the trusted choice in thousands of homes and businesses across Sydney for over 20 years, you can read more about our leading service level guarantee here, and from our other delighted customers here.</p>
    </section>

    <aside class="sidebar-card card-offers">
      <div class="card-title">Special Offers</div>
      <div class="card-photo" role="img" aria-label="Business people talking on phones in a bright corridor"></div>
    </aside>
    <aside class="sidebar-card card-reviews">
      <div class="card-title">Read our customer's reviews</div>
      <div class="card-photo" role="img" aria-label="Group of happy customers giving thumbs up"></div>
    </aside>

    <footer class="site-footer">
      <div class="copyright">Copyright © 2010 Veltrix</div>
      <div class="footer-sep"></div>
      <div class="footer-links">Links | Disclaimer | Privacy Poilcy | Contact Us</div>
    </footer>
  </div>
</body>
</html>
```